RA Infrastructure Capability Statement

I need to design a two page Capability statement for our Civil Construction company that looks professional and can be issued to clients in electronic or print form to show our capabilities.

We have an existing Logo and website https://ra-infragroup.com.au/

It should include space for the below:
- Company heading/logo plus ABN, ACN and full contact details
- About Us – Mission, vision, values
- Our Service Offering / Core competencies
- Accreditations/certifications

Designs look the same

```html
<!DOCTYPE html>
<html lang="en">
<head>
<meta charset="utf-8">
<title>RA Infrastructure – Capability Statement</title>
<link rel="stylesheet" href="https://fonts.googleapis.com/css2?family=Michroma&family=Arimo:wght@400;700&family=Roboto+Condensed:wght@400;700&display=swap">
<style>
  :root {
    --navy: #25287a;
    --orange: #f6ae1f;
    --orange-deep: #e0960f;
    --ink: #2a2a36;
    --paper: #ffffff;
    --backdrop: #b3b3b3;
    --photo-a: #8a96a6;
    --photo-b: #d9dde2;
  }
  * { box-sizing: border-box; margin: 0; padding: 0; }
  html, body { width: 1200px; height: 900px; overflow: hidden; }
  body {
    background: var(--backdrop);
    font-family: "Arimo", Arial, sans-serif;
    color: var(--ink);
    position: relative;
  }
  .page {
    position: absolute;
    top: 150px;
    width: 420px;
    height: 594px;
    background: var(--paper);
    overflow: hidden;
    box-shadow: 0 10px 30px rgba(0,0,0,.25);
  }
  .page--back { left: 150px; }
  .page--front { left: 630px; }
  .page__shapes { position: absolute; inset: 0; width: 100%; height: 100%; }

  .heading {
    font-family: "Michroma", sans-serif;
    color: var(--navy);
    text-transform: uppercase;
    line-height: 1.1;
    letter-spacing: .02em;
  }
  .heading--sub { color: var(--orange); }
  .body-text { font-size: 6px; line-height: 1.4; }

  .bullets { list-style: none; font-size: 5.8px; line-height: 1.42; }
  .bullets li { position: relative; padding-left: 8px; }
  .bullets li::before {
    content: ""; position: absolute; left: 0; top: 2px;
    border-left: 4px solid var(--orange);
    border-top: 2.2px solid transparent; border-bottom: 2.2px solid transparent;
  }

  /* front page */
  .brand {
    position: absolute; top: 16px; left: 120px;
    display: flex; align-items: center; gap: 7px;
  }
  .brand__square { width: 18px; height: 18px; background: var(--navy); }
  .brand__name {
    font-family: "Michroma", sans-serif; font-size: 13px;
    color: var(--navy); letter-spacing: .03em;
  }
  .hero-photo {
    position: absolute; left: 22px; top: 54px; width: 360px; height: 196px;
    background: linear-gradient(135deg, var(--photo-a), var(--photo-b) 70%, #f0f0f0);
    border: 4px solid var(--paper);
  }
  .title { position: absolute; left: 24px; top: 258px; }
  .title .heading { font-size: 17px; }
  .title .heading--sub { font-size: 14px; margin-top: 1px; }

  .col { position: absolute; }
  .col--left { left: 24px; top: 306px; width: 190px; }
  .col--right { left: 226px; top: 306px; width: 172px; }
  .col .heading { font-size: 10px; margin-bottom: 3px; }
  .col .heading--sub { font-size: 8px; margin-bottom: 3px; }
  .col .body-text { margin-bottom: 7px; }
  .col .bullets { margin-bottom: 10px; }

  /* back page */
  .back-content { position: absolute; left: 26px; top: 46px; width: 370px; }
  .back-content .heading { font-size: 13px; margin-bottom: 6px; }
  .back-content .body-text { margin-bottom: 12px; }
  .why-title { text-align: center; font-size: 15px !important; margin: 4px 0 20px !important; }

  .features { position: relative; height: 200px; }
  .feature {
    position: absolute; width: 160px; padding: 18px 10px 10px;
    border: 1.2px solid var(--navy); border-radius: 3px;
    font-size: 6px; line-height: 1.45; background: var(--paper);
  }
  .feature__icon {
    position: absolute; top: -13px; left: 50%; transform: translateX(-50%);
    width: 26px; height: 26px; border-radius: 50%; background: var(--navy);
    display: flex; align-items: center; justify-content: center;
  }
  .feature__title { font-weight: 700; display: block; margin-bottom: 2px; }
  .feature--one { left: 10px; top: 0; }
  .feature--two { left: 40px; top: 104px; }
  .feature--three { left: 210px; top: 52px; }

  .contact { position: absolute; left: 26px; bottom: 28px; width: 370px; }
  .contact .heading { font-size: 16px; text-align: center; margin-bottom: 10px; }
  .contact__grid {
    display: grid; grid-template-columns: 1fr 1fr; gap: 6px 16px;
    font-family: "Roboto Condensed", sans-serif; font-size: 8px; color: var(--navy);
  }
  .contact__item { display: flex; align-items: center; gap: 5px; }
  .contact__icon { width: 11px; height: 11px; flex: none; }
  .contact__label { font-weight: 700; }
</style>
</head>
<body>

<section class="page page--back">
  <svg class="page__shapes" viewBox="0 0 420 594" aria-hidden="true">
    <polygon points="170,0 420,0 420,38 140,38" fill="var(--orange)"/>
    <polygon points="0,0 34,0 0,34" fill="var(--navy)"/>
    <polygon points="0,560 0,594 34,594" fill="var(--navy)"/>
    <polygon points="420,556 420,594 382,594" fill="var(--orange-deep)"/>
  </svg>

  <div class="back-content">
    <h2 class="heading">Project<br>Program Management</h2>
    <p class="body-text">As a business we are focused on delivering for our clients from a project's inception to its completion. Our team have a deep understanding of engineering and construction principles and couple this with exceptional communication and reporting, which is the core of our service offering. We are a passionate group who are constantly striving to exceed best practice and find innovative ways to solve the inevitable challenges faced in construction. Our strength lies in our complex problem solving abilities and ongoing commitment to deliver projects on-time, on-budget to a high quality standard, all with safety being a constant focus. Our staff have managed large projects and programs of work and thus appreciate the main drivers and key performance indicators that must be monitored and managed on an ongoing basis. Additionally, our business has robust sub-contractor management processes which enable us to take on a broader range of projects while upholding high standards of work.</p>

    <h2 class="heading">Utilities</h2>
    <p class="body-text">Our team has a wide-ranging utilities background which gives us a deep understanding of what is in the ground and the requirements for each individual asset. Through this experience we have developed relationships with authorities to ensure we deliver projects that will stand the test of time, and we are a valuable piece of future network quality. This has further strengthened these relationships and puts us in a position to be a trusted advisor on the issues faced.</p>

    <h2 class="heading why-title">Why Choose Us</h2>
    <div class="features">
      <div class="feature feature--one">
        <span class="feature__icon"><svg width="12" height="12" viewBox="0 0 12 12" aria-hidden="true"><circle cx="6" cy="4" r="2.4" fill="#fff"/><path d="M1.5 11.5c0-3 2-4.5 4.5-4.5s4.5 1.5 4.5 4.5z" fill="#fff"/></svg></span>
        <span class="feature__title">Trusted Professionals</span>
        With a team of project professionals and field staff with countless years of experience, you can rest assured that you are engaging a knowledgeable team that will deliver results.
      </div>
      <div class="feature feature--three">
        <span class="feature__icon"><svg width="12" height="12" viewBox="0 0 12 12" aria-hidden="true"><path d="M2.5 6.2l2.3 2.3 4.7-5" fill="none" stroke="#fff" stroke-width="1.5"/></svg></span>
        <span class="feature__title">Collaborative Problem Solving</span>
        We believe we have the right people in place to be 'problem solvers' for our clients and are focused on delivering whatever services are required to make their lives easier.
      </div>
      <div class="feature feature--two">
        <span class="feature__icon"><svg width="12" height="12" viewBox="0 0 12 12" aria-hidden="true"><circle cx="6" cy="5" r="3.4" fill="none" stroke="#fff" stroke-width="1.3"/><path d="M4 8l-1 3.5 3-1.4 3 1.4-1-3.5" fill="#fff"/></svg></span>
        <span class="feature__title">Quality Assurance</span>
        We appreciate the nuances of each individual project, while ensuring all relevant processes and procedures are understood and followed. This is critical to the success of any project and the longevity of the assets being installed.
      </div>
    </div>
  </div>

  <div class="contact">
    <h2 class="heading">Contact Us</h2>
    <div class="contact__grid">
      <div class="contact__item">
        <svg class="contact__icon" viewBox="0 0 12 12" aria-hidden="true"><circle cx="6" cy="6" r="6" fill="var(--orange)"/><path d="M6 2.5a2.3 2.3 0 0 0-2.3 2.3c0 1.7 2.3 4.4 2.3 4.4s2.3-2.7 2.3-4.4A2.3 2.3 0 0 0 6 2.5z" fill="var(--navy)"/></svg>
        5/18 Kestrel Road, Derrimut VIC 3026
      </div>
      <div class="contact__item">
        <svg class="contact__icon" viewBox="0 0 12 12" aria-hidden="true"><circle cx="6" cy="6" r="6" fill="var(--orange)"/><rect x="2.8" y="3.8" width="6.4" height="4.4" fill="var(--navy)"/><path d="M2.8 3.8L6 6.3l3.2-2.5" fill="none" stroke="var(--orange)" stroke-width=".7"/></svg>
        tenders@ra-infragroup.com.au
      </div>
      <div class="contact__item">
        <span><span class="contact__label">ABN :</span> 00 000 000 000<br><span class="contact__label">ACN :</span> 000 000 000</span>
      </div>
      <div class="contact__item">
        <svg class="contact__icon" viewBox="0 0 12 12" aria-hidden="true"><circle cx="6" cy="6" r="6" fill="var(--navy)"/><path d="M4 3l1.2 1.6-.7.8a4 4 0 0 0 2.1 2.1l.8-.7L9 8l-.8 1C5.6 8.8 3.2 6.4 3 3.8z" fill="var(--orange)"/></svg>
        <span>Daniel Hayes 0400 118 240<br>Mark Ellison 0400 662 917</span>
      </div>
    </div>
  </div>
</section>

<section class="page page--front">
  <svg class="page__shapes" viewBox="0 0 420 594" aria-hidden="true">
    <polygon points="0,0 40,0 0,40" fill="var(--navy)"/>
    <polygon points="300,42 420,42 420,262 400,290 360,290 360,54" fill="var(--orange)"/>
    <polygon points="420,550 420,594 372,594" fill="var(--orange)"/>
  </svg>

  <div class="brand">
    <span class="brand__square"></span>
    <span class="brand__name">RA INFRASTRUCTURE</span>
  </div>

  <div class="hero-photo" role="img" aria-label="Photo of engineers discussing plans over a white hard hat on a site office desk"></div>

  <div class="title">
    <h1 class="heading">RA Infrastructure</h1>
    <p class="heading heading--sub">Capability Statement</p>
  </div>

  <div class="col col--left">
    <h2 class="heading">About Us</h2>
    <p class="body-text">Tier 1 engineering and project management capability with nimble privately owned and operated mentality. RA Infrastructure is a specialist utilities contractor leveraging industry experience to provide exceptional outcomes. We are a client focused business that takes a 'best-for-project' approach in everything we do, and see honest, timely and transparent communication as one of our key strengths. Our business works in complex, high-risk environments and understands all safety, quality and environmental considerations.</p>

    <h2 class="heading">Our Service Offering</h2>
    <p class="heading heading--sub">Water Infrastructure</p>
    <ul class="bullets">
      <li>Accredited contractor with major Water Authorities</li>
      <li>Constructability design reviews from highly experienced professionals</li>
      <li>Reticulation mains and larger pipelines</li>
      <li>Experienced with PVC, Polyethylene, Ductile Iron, GRP and Mild Steel</li>
      <li>Butt welding of PE pipelines</li>
      <li>Domestic water services</li>
      <li>Meter assemblies</li>
      <li>Relocation of existing water assets</li>
      <li>Dedicated commissioning crew for Swabbing, Hydrostatic Testing, Chlorinating and Water Quality Testing</li>
      <li>Complex live connections</li>
    </ul>
  </div>

  <div class="col col--right">
    <h2 class="heading">Gas<br>Infrastructure</h2>
    <ul class="bullets">
      <li>Accredited contractor that can work on major Gas Authorities networks</li>
      <li>Constructability design reviews from highly experienced professionals</li>
      <li>Reticulation mains in single or common trench and larger pipelines</li>
      <li>Butt welding and electro-fusion</li>
      <li>Pre-laid gas services</li>
      <li>Pressure testing</li>
      <li>Complex gas tie-ins</li>
    </ul>

    <h2 class="heading">Civil<br>Construction</h2>
    <p class="body-text">Outside the Utilities space we can assist with an array of civil construction works and have proven capabilities in the below areas.</p>
    <ul class="bullets">
      <li>Bulk earthworks</li>
      <li>Rehabilitation works</li>
      <li>Detailed excavations</li>
      <li>Hydro Excavation and underground service locating</li>
      <li>Landscaping</li>
      <li>General Civil works</li>
    </ul>
  </div>
</section>

</body>
</html>
```